Wanted: A Simple yet Awesome Blog Hero Image

We need a hero image (blog graphic header) to replace our existing one: https://www.terravexlab.com//blog/soil-classification-foundation-and-pavement-design-starts-here
Want something to reflect what the blog article is about and is a reflection of the title.

Note: we are not in love with any of our hero graphics

Industry/Entity Type

Construction

Colors

Designer to choose colors to be used in the design.

Requirements
Must have
• Width must be 715px
• Height must not exceed 400px
• Content on graphic should be: Soil Classification: Foundation and Pavement Design Starts Here
Nice to have
• a product shown that is mentioned in the blog
Should not have
• a product with a Carrowmere logo

```html
<!DOCTYPE html>
<html lang="en">
<head>
<meta charset="utf-8">
<title>Soil Classification – Blog Hero</title>
<link href="https://fonts.googleapis.com/css2?family=Tenor+Sans&display=swap" rel="stylesheet">
<style>
  :root {
    --page-bg: #e4e5e8;
    --hero-deep: #3a1a6e;
    --hero-violet: #4b2490;
    --hero-plum: #6a1f7a;
    --hero-magenta: #8a2483;
    --text-light: #ffffff;
    --text-faint: rgba(255, 255, 255, 0.16);
    --product-silver: #b9b6c4;
    --product-shadow: #5b3f8c;
  }
  * { margin: 0; padding: 0; box-sizing: border-box; }
  html, body {
    width: 1012px;
    height: 1200px;
    overflow: hidden;
    background: var(--page-bg);
  }
  .canvas {
    position: relative;
    width: 1012px;
    height: 1200px;
  }
  .blog-hero {
    position: absolute;
    left: 36px;
    top: 371px;
    width: 940px;
    height: 458px;
    overflow: hidden;
    font-family: "Tenor Sans", sans-serif;
    color: var(--text-light);
    background:
      radial-gradient(ellipse 60% 70% at 15% 95%, var(--hero-magenta) 0%, transparent 70%),
      linear-gradient(120deg, var(--hero-deep) 0%, var(--hero-plum) 45%, var(--hero-violet) 75%, var(--hero-deep) 100%);
    box-shadow: 0 18px 40px rgba(0, 0, 0, 0.22);
  }
  .hero-light-band {
    position: absolute;
    inset: 0;
    width: 100%;
    height: 100%;
  }
  .hero-title {
    position: absolute;
    left: 67px;
    top: 58px;
    font-size: 52px;
    font-weight: 400;
    line-height: 1;
    letter-spacing: 0.5px;
  }
  .hero-subtitle {
    position: absolute;
    left: 67px;
    top: 120px;
    font-size: 29px;
    font-weight: 400;
    line-height: 33px;
    letter-spacing: 0.3px;
  }
  .product-visual {
    position: absolute;
    left: 378px;
    top: 107px;
    width: 522px;
    height: 303px;
    border-radius: 10px;
    background:
      radial-gradient(ellipse 55% 60% at 72% 38%, rgba(240, 232, 214, 0.55) 0%, transparent 70%),
      radial-gradient(ellipse 60% 30% at 45% 82%, rgba(200, 198, 210, 0.5) 0%, transparent 75%),
      linear-gradient(160deg, transparent 0%, rgba(185, 182, 196, 0.18) 60%, transparent 100%);
  }
  .hero-tag {
    position: absolute;
    right: 20px;
    bottom: 14px;
    font-size: 19px;
    letter-spacing: 0.5px;
    color: var(--text-faint);
  }
</style>
</head>
<body>
  <main class="canvas">
    <section class="blog-hero" aria-label="Soil Classification blog hero">
      <svg class="hero-light-band" viewBox="0 0 940 458" preserveAspectRatio="none" aria-hidden="true">
        <polygon points="600,0 940,0 940,458 760,458" fill="#ffffff" opacity="0.04"/>
        <polygon points="700,0 800,0 940,300 940,458" fill="#ffffff" opacity="0.03"/>
      </svg>
      <h1 class="hero-title">Soil Classification</h1>
      <p class="hero-subtitle">Foundation and Pavement<br>Design Starts Here</p>
      <div class="product-visual" role="img" aria-label="Soil testing equipment: an open soil colour chart book, test sieves, a pocket penetrometer, a vane tester and a dial gauge"></div>
      <span class="hero-tag">SOIL CLASSIFICATION</span>
    </section>
  </main>
</body>
</html>
```